Venture Wreckers Book Needs a Cover Design

We need a cover design for Venture Wreckers, Practical Guidance for Faltering Ventures and Doubting Company Founders. We will publish and ebook first (first priority), followed by a hard cover printed book, and then a soft cover book after a few months. The book includes 40 Venture Wreckers and actions owners can implement to counter them and grow. Some examples of killers: self-sabotage, wild optimism, scamming, addictions, burnout, no plan, procrastination, recklessness, haemorrhaging money, etc. We plan to publish the ebook to Pagelume / Tarvelo standards. We want to see designs that convey professionalism, simplicity and creativity.

Target Market(s)

Small and microbusinesses, including start-ups, proprietorships, cottage industries, home-based, single operator, and businesses with or without employees, including corporations and partnerships with fewer than five employees

Industry/Entity Type

Business

Font styles to use
Sans Serif

Colors

Designer to choose colors to be used in the design.

Requirements
Must have
• Uncluttered, professional
• Title: Venture Wreckers
• Subtitle: Practical Guidance for Faltering Ventures and Doubting Company Founders
• Author: Mel Hartigan
Nice to have
• n/a

```html
<!DOCTYPE html>
<html lang="en">
<head>
<meta charset="utf-8">
<title>Venture Wreckers – Book Cover</title>
<link rel="stylesheet" href="https://fonts.googleapis.com/css2?family=Bebas+Neue&family=PT+Serif&display=swap">
<style>
  :root {
    --cover-black: #000000;
    --silver-light: #f2f2f2;
    --silver-mid: #bdbdbd;
    --silver-dark: #7d7d7d;
    --title-red: #c0101c;
    --glove-red: #b3121d;
    --glove-shadow: #3a0508;
    --pattern-grey: #1c1c1c;
    --subtitle-white: #ffffff;
  }
  html, body {
    margin: 0;
    padding: 0;
    width: 772px;
    height: 1200px;
    overflow: hidden;
    background: var(--cover-black);
  }
  .cover {
    display: block;
    width: 772px;
    height: 1200px;
  }
  .title-word,
  .author-name {
    font-family: "Bebas Neue", "Oswald", sans-serif;
  }
  .title-word--top { fill: url(#silverFill); }
  .title-word--bottom { fill: var(--title-red); }
  .author-name { fill: url(#silverFill); }
  .subtitle {
    font-family: "PT Serif", "Georgia", serif;
    font-size: 36px;
    fill: var(--subtitle-white);
  }
  .stop-light { stop-color: var(--silver-light); }
  .stop-mid { stop-color: var(--silver-mid); }
  .stop-dark { stop-color: var(--silver-dark); }
  .stop-pattern { stop-color: var(--pattern-grey); }
  .stop-pattern-fade { stop-color: var(--cover-black); }
  .stop-glove { stop-color: var(--glove-red); }
  .stop-glove-shadow { stop-color: var(--glove-shadow); }
  .stop-black { stop-color: var(--cover-black); }
</style>
</head>
<body>
<svg class="cover" viewBox="0 0 772 1200" xmlns="http://www.w3.org/2000/svg">
  <defs>
    <linearGradient id="silverFill" x1="0" y1="0" x2="0" y2="1">
      <stop offset="0" class="stop-light"/>
      <stop offset="0.5" class="stop-mid"/>
      <stop offset="1" class="stop-dark"/>
    </linearGradient>
    <linearGradient id="patternTopFade" x1="0" y1="0" x2="0" y2="1">
      <stop offset="0" class="stop-pattern"/>
      <stop offset="1" class="stop-pattern-fade"/>
    </linearGradient>
    <linearGradient id="patternBottomFade" x1="0" y1="1" x2="0" y2="0">
      <stop offset="0" class="stop-pattern"/>
      <stop offset="1" class="stop-pattern-fade"/>
    </linearGradient>
    <radialGradient id="gloveGlow" cx="0.5" cy="0.45" r="0.55">
      <stop offset="0" class="stop-glove"/>
      <stop offset="0.65" class="stop-glove-shadow"/>
      <stop offset="1" class="stop-black"/>
    </radialGradient>
  </defs>

  <rect class="cover-background" width="772" height="1200" fill="var(--cover-black)"/>

  <rect class="pattern-band pattern-band--top" x="0" y="0" width="772" height="80"
        fill="url(#patternTopFade)" role="img" aria-label="Faint dark triangle pattern along the top edge"/>
  <rect class="pattern-band pattern-band--bottom" x="0" y="1040" width="772" height="160"
        fill="url(#patternBottomFade)" role="img" aria-label="Faint dark triangle pattern along the bottom edge"/>

  <g class="title">
    <text class="title-word title-word--top" x="100" y="240" font-size="220"
          textLength="553" lengthAdjust="spacingAndGlyphs">VENTURE</text>
    <text class="title-word title-word--bottom" x="115" y="413" font-size="220"
          textLength="538" lengthAdjust="spacingAndGlyphs">WRECKERS</text>
  </g>

  <rect class="glove-photo" x="0" y="550" width="772" height="310" fill="url(#gloveGlow)"
        role="img" aria-label="Photograph of two red boxing gloves touching in the centre"/>

  <text class="subtitle" text-anchor="middle">
    <tspan x="386" y="640">Practical Guidance for</tspan>
    <tspan x="386" y="694">Faltering Ventures and</tspan>
    <tspan x="386" y="748">Doubting Company</tspan>
    <tspan x="386" y="802">Founders</tspan>
  </text>

  <text class="author-name" x="178" y="1138" textLength="427" lengthAdjust="spacingAndGlyphs">
    <tspan font-size="107">M</tspan><tspan font-size="90">EL </tspan><tspan font-size="107">H</tspan><tspan font-size="90">ARTIGAN</tspan>
  </text>
</svg>
</body>
</html>
```